Harbourline construction company Business card design

I need a business card design for my company. I have a logo but dont have business cards with our logo..

www.harbourlineconstructco.com.au

The logo is on the website

I need the same details as this design I have attached. we have changed the logo and colours. just like the website

Industry/Entity Type

Building

```html
<!DOCTYPE html>
<html lang="en">
<head>
<meta charset="utf-8">
<title>Harbourline Construction – Business Card</title>
<link rel="stylesheet" href="https://fonts.googleapis.com/css2?family=Cinzel:wght@400;600&family=Open+Sans:wght@400;600&family=Tinos:wght@700&display=swap">
<style>
  :root {
    --bg: #eceae6;
    --card: #ffffff;
    --blue: #2f93cf;
    --grey: #b3b5b8;
    --ink: #111111;
    --text: #1c1c1c;
  }
  * { box-sizing: border-box; margin: 0; padding: 0; }
  html, body { width: 1200px; height: 1000px; overflow: hidden; background: var(--bg); }
  .card {
    position: absolute; left: 100px; top: 200px; width: 1000px; height: 600px;
    background: var(--card); border-radius: 44px; overflow: hidden;
    box-shadow: 0 14px 40px rgba(0,0,0,.14);
  }
  .band-blue { position: absolute; left: 0; right: 0; top: 690px; top: 490px; height: 72px; background: var(--blue); }
  .band-grey { position: absolute; left: 0; right: 0; top: 562px; height: 38px; background: var(--grey); }

  .brand { position: absolute; left: 40px; top: 110px; width: 400px; text-align: center; }
  .brand-mark { width: 70px; height: 70px; background: var(--blue); margin: 0 auto 26px; }
  .brand-name {
    font-family: 'Cinzel', serif; font-weight: 600; color: var(--blue);
    font-size: 40px; line-height: 1.1; letter-spacing: 2px;
  }
  .brand-rule { width: 340px; height: 4px; background: var(--ink); margin: 20px auto 16px; }
  .tagline {
    font-family: 'Tinos', serif; font-weight: 700; color: var(--ink);
    font-size: 23px; line-height: 1.3;
  }

  .divider { position: absolute; left: 475px; top: 60px; width: 3px; height: 350px; background: var(--blue); }

  .person { position: absolute; left: 530px; top: 62px; }
  .person-name { font-family: 'Cinzel', serif; font-size: 34px; color: var(--ink); letter-spacing: 1px; }
  .person-role { font-family: 'Tinos', serif; font-weight: 700; color: var(--blue); font-size: 19px; margin: 2px 0 0 170px; }

  .contacts { position: absolute; left: 530px; top: 190px; list-style: none; }
  .contacts li { display: flex; align-items: center; height: 40px; font-family: 'Open Sans', sans-serif; color: var(--text); font-size: 19px; }
  .contacts li.wide { letter-spacing: 4px; }
  .contacts li.address { height: 58px; line-height: 1.2; }
  .contacts svg { width: 30px; height: 30px; margin-right: 18px; flex: none; fill: var(--blue); }
</style>
</head>
<body>
  <div class="card">
    <div class="brand">
      <div class="brand-mark"></div>
      <div class="brand-name">HARBOURLINE<br>CONSTRUCTION</div>
      <div class="brand-rule"></div>
      <p class="tagline">New Homes-Additions &amp; Renovations<br>Domestic &amp; Commercial Builders</p>
    </div>

    <div class="divider"></div>

    <div class="person">
      <div class="person-name">Marek Dalton</div>
      <div class="person-role">Director</div>
    </div>

    <ul class="contacts">
      <li class="wide">
        <svg viewBox="0 0 30 30"><rect x="3" y="9" width="24" height="18" rx="3"/><rect x="6" y="4" width="18" height="7" rx="3"/><rect x="9" y="14" width="12" height="9" fill="#fff"/></svg>
        9152 4730
      </li>
      <li class="wide">
        <svg viewBox="0 0 30 30"><rect x="8" y="2" width="14" height="26" rx="3"/><rect x="10" y="6" width="10" height="16" fill="#fff"/></svg>
        0412 556 093
      </li>
      <li>
        <svg viewBox="0 0 30 30"><rect x="2" y="7" width="26" height="17"/><path d="M2 7 L15 17 L28 7" fill="none" stroke="#fff" stroke-width="2"/></svg>
        info@harbourlineconstructco.com.au
      </li>
      <li>
        <svg viewBox="0 0 30 30"><circle cx="15" cy="15" r="12"/><g fill="none" stroke="#fff" stroke-width="1.6"><ellipse cx="15" cy="15" rx="5" ry="12"/><line x1="3" y1="15" x2="27" y2="15"/><line x1="5" y1="9" x2="25" y2="9"/><line x1="5" y1="21" x2="25" y2="21"/></g></svg>
        www.harbourlineconstructco.com.au
      </li>
      <li class="address">
        <svg viewBox="0 0 30 30"><rect x="3" y="10" width="24" height="18" rx="3"/><path d="M15 2 a6 6 0 0 1 6 6 c0 5 -6 10 -6 10 s-6 -5 -6 -10 a6 6 0 0 1 6 -6z" fill="#fff"/><circle cx="15" cy="8" r="3"/></svg>
        <span>Unit 4 Level 2, 18 Marlowe<br>Ave, Westmere Cove, WA 6035</span>
      </li>
    </ul>

    <div class="band-blue"></div>
    <div class="band-grey"></div>
  </div>
</body>
</html>
```